Public Relations Agency Seeks Wordpress Design and Coding

TORVEX Media is a public relations agency specializing in media relations, public affairs and marketing communication.

The site should display the following visual characteristics: professionalism, trustworthiness, high-tech focus, clear and concise design.

The desired colors are royal blue, gray and hints of red.

Design look/feel inspired by this site: http://brisklanefetes.example/

Specifications:

1. Navigation/Pages/Index:

HOME

ABOUT US

SERVICES

NEWS

CONTACT

---

2. Functionality of/content for each page:

- Home
o Dominant photo (professional, edgy, innovative)
o Simple, straightforward access to/from “Home” from other pages
o Includes logo (attached) and tagline "Amplify every message that matters"
o Direct link to “CONTACT”
o Links to social media accounts: Facebook, Twitter, LinkedIn

- About Us

o Company profile blurb
o President’s photo with short bio

- Services
o Public Relations
 Strategic communication
 Brand and reputation management
 Community relations
o Media Relations
 News coverage and contacts
 Media training and interview skills
 Crisis communications
o Congressional Affairs
 Public affairs
 Public policy
 Legislative strategy
o Mass Communication
 Speechwriting
 Presentation creation
 Social media
o Marketing Communications
 Business collateral material
 Promotional campaigns
 Special events and tradeshows

- News
o Blog-like page to post information and/or share news from other sites

- Contact
o Standard “Contact Us” form (Name, Email, Phone, Message)
o Direct Contact
 (555) 314-2690
 Marlow@TORVEXmedia.example

Target Market(s)

Small to large businesses specializing in high technology, defense/military, medicine/healthcare, and wide array of professional services.

Industry/Entity Type

Marketing

Font styles to use
Serif
Sans Serif

Colors
0555a3
ec2027
edf3f7

Requirements
Must have
• -- Project reqires DESIGN - and - fully CODED.

-- Strong SEO

-- Optimized for mobile viewing

Thank you!

```html
<!DOCTYPE html>
<html lang="en">
<head>
<meta charset="utf-8">
<title>TORVEX Media — Amplify every message that matters</title>
<link href="https://fonts.googleapis.com/css2?family=Open+Sans:ital,wght@0,300;0,400;0,600;0,700;1,400;1,600&family=Roboto+Condensed:wght@300;400;700&display=swap" rel="stylesheet">
<style>
:root{
  --blue:#0555a3;
  --red:#ec2027;
  --mist:#edf3f7;
  --ink:#4a4a4a;
  --muted:#7b7b7b;
  --line:#c9ccd0;
  --white:#ffffff;
  --social:#4a6b93;
}
*{margin:0;padding:0;box-sizing:border-box}
html,body{width:1200px;height:2267px;overflow:hidden}
body{font-family:"Open Sans",Arial,sans-serif;color:var(--ink);background:var(--white);position:relative}

/* header */
.site-header{position:absolute;left:0;top:0;width:1200px;height:98px;background:var(--mist)}
.brand{position:absolute;left:196px;top:18px}
.brand-name{font-weight:600;font-size:27px;color:#6d6e71;letter-spacing:1px;line-height:32px}
.brand-tagline{font-size:10.5px;font-weight:600;color:#555;margin-top:12px;white-space:nowrap}
.contact-strip{position:absolute;right:197px;top:18px;display:flex;gap:24px;font-size:11px;color:#444}
.contact-strip span{display:flex;align-items:center;gap:7px}
.main-nav{position:absolute;right:197px;top:50px;display:flex;font-size:15px;font-weight:600;color:#555}
.main-nav a{display:block;height:41px;line-height:41px;padding:0 0 0 42px;color:inherit;text-decoration:none}
.main-nav a.current{background:var(--red);color:var(--white);padding:0 19px}
.main-nav a.current + a{padding-left:24px}

/* hero */
.hero{position:absolute;left:0;top:98px;width:1200px;height:485px;background:linear-gradient(100deg,#5b5f66 0%,#8a8f96 35%,#b9bcc0 60%,#6f6a6a 85%,#4a4546 100%)}
.hero-shade{position:absolute;inset:0;background:rgba(20,22,26,.28)}
.hero-title{position:absolute;left:0;width:1200px;top:196px;text-align:center;font-weight:400;font-size:64px;color:var(--white);line-height:80px}
.hero-sub{position:absolute;left:0;width:1200px;top:279px;text-align:center;font-weight:600;font-size:20px;color:var(--white)}
.hero-btn{position:absolute;left:533px;top:346px;width:106px;height:37px;background:var(--red);color:var(--white);font-size:16px;text-align:center;line-height:37px}

/* section headings */
.section-title{position:absolute;font-family:"Roboto Condensed",Arial,sans-serif;font-weight:300;font-size:24px;color:#555;text-transform:uppercase;line-height:28px;white-space:nowrap}
.section-title strong{font-weight:400;color:var(--blue)}
.section-title::after{content:"";position:absolute;left:0;top:39px;width:124px;height:3px;background:linear-gradient(90deg,var(--line) 0 40%,var(--red) 40% 60%,var(--line) 60% 100%)}
.on-dark{color:var(--white);font-weight:400}

/* welcome */
.welcome-copy{position:absolute;left:196px;top:677px;width:454px;font-size:11.8px;line-height:19.5px;color:var(--muted)}
.welcome-copy p{margin-bottom:7px}
.president{position:absolute;left:669px;top:624px;width:334px;height:268px;background:linear-gradient(120deg,#3b3f47,#6b6f78 45%,#9c8e80 70%,#4b4e56)}
.president-caption{position:absolute;left:0;bottom:0;width:100%;height:46px;background:rgba(5,85,163,.85);color:var(--white);padding:6px 14px}
.president-caption b{display:block;font-size:13px;font-weight:600}
.president-caption span{font-size:9.5px;display:flex;align-items:center;gap:6px;white-space:nowrap}

/* services */
.services{position:absolute;left:0;top:932px;width:1200px;height:432px;background:var(--mist)}
.service-list{position:absolute;left:196px;top:79px;display:flex;gap:9px}
.service-card{width:154px;height:328px;background:var(--white);text-align:center;position:relative}
.service-card h3{font-size:14px;font-weight:600;color:#444;line-height:16px;margin-top:11px;height:32px;text-transform:uppercase}
.service-icon{display:block;margin:26px auto 0}
.service-items{position:absolute;left:12px;right:12px;top:186px;list-style:none;font-size:10.5px;line-height:13px;color:#666}
.service-items li{height:46px;padding-top:4px;border-bottom:1px dotted #ddd}
.service-card.featured{background:var(--red)}
.service-card.featured h3,.service-card.featured .service-items{color:var(--white)}
.service-card.featured .service-items li{border-bottom:1px dashed rgba(255,255,255,.7)}
.service-card .service-items li:last-child{border-bottom:none}

/* news */
.news-item{position:absolute;top:1458px;width:150px;font-size:11px;line-height:15px;color:var(--muted)}
.news-date{font-size:12px;font-weight:600;color:#333;margin-bottom:16px}
.news-title{color:var(--red);font-size:11.5px;margin-bottom:7px}
.more-btn{position:absolute;left:196px;top:1549px;width:73px;height:23px;background:var(--red);color:var(--white);font-size:11px;line-height:23px;text-align:center}
.divider{position:absolute;left:680px;top:1435px;width:1px;height:142px;background:#ddd}
.video-thumb{position:absolute;top:1459px;width:143px;height:113px;background:linear-gradient(135deg,#3a3d42,#6a6d72 55%,#2e3034);border:1px solid #222}
.video-thumb svg{position:absolute;left:53px;top:38px}

/* testimonials */
.testimonials{position:absolute;left:0;top:1614px;width:1200px;height:299px;background:linear-gradient(180deg,#3a3d43,#4b4d52 50%,#36383d)}
.client-photo{position:absolute;left:196px;top:1722px;width:102px;height:111px;background:linear-gradient(160deg,#d9d2cc,#a8958a 60%,#6b5d58)}
.quote{position:absolute;left:320px;top:1710px;width:683px;font-size:11.3px;line-height:20px;color:#e4e4e4}
.client-name{position:absolute;left:320px;top:1797px;color:var(--white);font-weight:700;font-size:13px}
.client-role{position:absolute;left:320px;top:1820px;color:var(--white);font-style:italic;font-weight:600;font-size:10px}
.dots{position:absolute;left:198px;top:1866px;display:flex;gap:5px}
.dots i{width:9px;height:9px;border-radius:50%;background:var(--white)}
.dots i.on{background:var(--red)}

/* contact */
.contact-intro{position:absolute;left:196px;top:2002px;width:807px;font-size:13.3px;line-height:19px;color:#555}
.field{position:absolute;left:196px;width:363px;height:28px;border:1px solid #c8c8c8;font-size:11px;color:#555;padding:6px 10px;background:var(--white)}
.field.message{left:580px;top:2060px;width:301px;height:98px}
.submit-btn{position:absolute;left:898px;top:2060px;width:105px;height:98px;background:var(--red);color:var(--white);font-weight:700;font-size:18px;text-align:center;line-height:98px;border-radius:3px}

/* footer */
.site-footer{position:absolute;left:0;top:2189px;width:1200px;height:78px;background:var(--mist)}
.footer-nav{position:absolute;left:196px;top:19px;font-size:10.5px;color:#555;display:flex;gap:9px}
.footer-nav .current{color:var(--blue)}
.copyright{position:absolute;left:196px;top:42px;font-size:11px;color:#666}
.social{position:absolute;left:598px;top:26px;display:flex;gap:8px}
.social span{width:20px;height:20px;background:var(--social)}
.footer-brand{position:absolute;right:197px;top:15px;text-align:right}
.footer-brand .brand-name{font-size:23px;line-height:28px}
.footer-brand .brand-tagline{font-size:9px;margin-top:6px;color:#333}
</style>
</head>
<body>

<header class="site-header">
  <div class="brand">
    <div class="brand-name">TORVEX Media</div>
    <div class="brand-tagline">Amplify every message that matters</div>
  </div>
  <div class="contact-strip">
    <span><svg width="12" height="14" viewBox="0 0 12 14"><path d="M3 1 L5 4 L3.8 5.5 C4.6 7.6 5.8 9 7.6 10 L9 8.8 L11.5 10.8 L10 13 C5 12.5 1.2 7.5 1 2.5 Z" fill="#0555a3"/></svg>(555) 314-2690</span>
    <span><svg width="16" height="11" viewBox="0 0 16 11"><rect x="0.5" y="0.5" width="15" height="10" fill="#0555a3"/><path d="M1 1 L8 6.5 L15 1" stroke="#fff" stroke-width="1.3" fill="none"/></svg>Marlow@TORVEXmedia.example</span>
  </div>
  <nav class="main-nav">
    <a class="current" href="#">HOME</a>
    <a href="#">ABOUT US</a>
    <a href="#">SERVICES</a>
    <a href="#">NEWS</a>
    <a href="#">CONTACT</a>
  </nav>
</header>

<section class="hero">
  <div class="hero-shade" role="img" aria-label="Speaker addressing an audience from a podium in a conference hall"></div>
  <h1 class="hero-title">I'm seeking a news media</h1>
  <p class="hero-sub">specializing in media relations, public affairs and marketing communication.</p>
  <div class="hero-btn">Read more</div>
</section>

<h2 class="section-title" style="left:196px;top:618px">Welcome to <strong>TORVEX Media</strong></h2>
<div class="welcome-copy">
  <p>Lorem ipsum dolor sit amet, consectetur adipiscing elit. Phasellus faucibus congue purus, non eleifend ex tempus id. Curabitur tincidunt, sapien ut rhoncus luctus, ex odio congue nulla, ut ultricies ex lacus eu felis. Nunc a nisl venenatis, accumsan nisi at, ornare ex. Vivamus elementum enim a magna.</p>
  <p>Duis finibus, dolor id consequat malesuada, urna tellus facilisis mauris, sit amet suscipit purus arcu quis ex. Nulla facilisi. Integer in commodo metus. Lorem ipsum dolor sit amet, consectetur adipiscing elit.</p>
  <p>Phasellus faucibus congue purus, non eleifend ex tempus id. Curabitur tincidunt, sapien ut rhoncus luctus, ex odio congue nulla, ut ultricies ex lacus eu felis. Nunc a nisl venenatis, accumsan nisi at, ornare exdo metus.</p>
</div>
<figure class="president" role="img" aria-label="Portrait of the agency president in front of a flag">
  <figcaption class="president-caption">
    <b>MEET TORVEX MEDIA PRESIDENT</b>
    <span>Ashford Marlow is torvex President on Lorem ipsum dolor sit
      <svg width="10" height="10" viewBox="0 0 10 10"><circle cx="5" cy="5" r="5" fill="#fff"/><path d="M4 2.8 L6.2 5 L4 7.2" stroke="#0555a3" stroke-width="1.4" fill="none"/></svg></span>
  </figcaption>
</figure>

<section class="services">
  <h2 class="section-title" style="left:196px;top:20px">Our <strong>Services</strong></h2>
  <div class="service-list">
    <article class="service-card featured">
      <h3>Public<br>Relations</h3>
      <svg class="service-icon" width="106" height="106" viewBox="0 0 106 106" role="img" aria-label="Public relations icon"><circle cx="53" cy="53" r="50" fill="none" stroke="#fff" stroke-width="3"/><circle cx="53" cy="53" r="44" fill="#fff"/><circle cx="53" cy="53" r="20" fill="#ec2027"/></svg>
      <ul class="service-items"><li>Strategic<br>Communication</li><li>Brand and Reputation<br>Management</li><li>Community<br>Relations</li></ul>
    </article>
    <article class="service-card">
      <h3>Media<br>Relations</h3>
      <svg class="service-icon" width="106" height="106" viewBox="0 0 106 106" role="img" aria-label="Media relations icon"><circle cx="53" cy="53" r="50" fill="none" stroke="#ec2027" stroke-width="3"/><circle cx="53" cy="53" r="44" fill="#ec2027"/><circle cx="53" cy="53" r="20" fill="#fff"/></svg>
      <ul class="service-items"><li>News Coverage<br>And Contacts</li><li>Media Training and<br>interview Skills</li><li>Crisis<br>Communications</li></ul>
    </article>
    <article class="service-card">
      <h3>Congressional<br>Affairs</h3>
      <svg class="service-icon" width="106" height="106" viewBox="0 0 106 106" role="img" aria-label="Congressional affairs icon"><circle cx="53" cy="53" r="50" fill="none" stroke="#ec2027" stroke-width="3"/><circle cx="53" cy="53" r="44" fill="#ec2027"/><circle cx="53" cy="53" r="20" fill="#fff"/></svg>
      <ul class="service-items"><li>Public<br>Affairs</li><li>Public<br>Policy</li><li>Legislative<br>Strategy</li></ul>
    </article>
    <article class="service-card">
      <h3>Mass<br>Communication</h3>
      <svg class="service-icon" width="106" height="106" viewBox="0 0 106 106" role="img" aria-label="Mass communication icon"><circle cx="53" cy="53" r="50" fill="none" stroke="#ec2027" stroke-width="3"/><circle cx="53" cy="53" r="44" fill="#ec2027"/><circle cx="53" cy="53" r="20" fill="#fff"/></svg>
      <ul class="service-items"><li>Speech<br>Writing</li><li>Presentation<br>Creation</li><li>Social<br>Media</li></ul>
    </article>
    <article class="service-card">
      <h3>Marketing<br>Communications</h3>
      <svg class="service-icon" width="106" height="106" viewBox="0 0 106 106" role="img" aria-label="Marketing communications icon"><circle cx="53" cy="53" r="50" fill="none" stroke="#ec2027" stroke-width="3"/><circle cx="53" cy="53" r="44" fill="#ec2027"/><circle cx="53" cy="53" r="20" fill="#fff"/></svg>
      <ul class="service-items"><li>Business Collateral<br>Material</li><li>Promotional<br>Campaigns</li><li>Special events<br>and tradeshows</li></ul>
    </article>
  </div>
</section>

<h2 class="section-title" style="left:196px;top:1400px">Latest <strong>News</strong></h2>
<article class="news-item" style="left:196px"><div class="news-date">29. 09. 2014</div><div class="news-title">News Coverage And</div>Lorem ipsum dolor sit amet, consectetur adipiscing elit.</article>
<article class="news-item" style="left:361px"><div class="news-date">29. 09. 2014</div><div class="news-title">Vivamus turpis justo,</div>Lorem ipsum dolor sit amet, consectetur adipiscing elit.</article>
<article class="news-item" style="left:527px"><div class="news-date">29. 09. 2014</div><div class="news-title">News Coverage And</div>Lorem ipsum dolor sit amet, consectetur adipiscing elit.</article>
<div class="more-btn">More News</div>
<div class="divider"></div>

<h2 class="section-title" style="left:701px;top:1400px">Recent <strong>Video</strong></h2>
<div class="video-thumb" style="left:701px" role="img" aria-label="Video still of a business meeting">
  <svg width="36" height="36" viewBox="0 0 36 36"><circle cx="18" cy="18" r="16" fill="none" stroke="#fff" stroke-width="2"/><path d="M15 12 L23 18 L15 24 Z" fill="#fff"/></svg>
</div>
<div class="video-thumb" style="left:861px" role="img" aria-label="Video still of a team discussion">
  <svg width="36" height="36" viewBox="0 0 36 36"><circle cx="18" cy="18" r="16" fill="none" stroke="#fff" stroke-width="2"/><path d="M15 12 L23 18 L15 24 Z" fill="#fff"/></svg>
</div>

<section class="testimonials" role="img" aria-label="Blurred crowd of people in the background"></section>
<h2 class="section-title on-dark" style="left:196px;top:1648px">What say our clients</h2>
<div class="client-photo" role="img" aria-label="Portrait of the client"></div>
<blockquote class="quote">“ Stet clita kasd gubergren, no sea takimata sanctus est Lorem ipsum dolor sit amet. Lorem ipsum dolor sit amet, consetetur sadip scing dolarelitr, sed diam nonumy eirmod tempor invidunt ut labore et dolore magna aliquyam erat, sed diam voluptua. At vero e os et accusam et dols justo duo dolores et ea rebum.”</blockquote>
<div class="client-name">Miss Lorem dolar</div>
<div class="client-role">Sale Manager at Vantor Corp.</div>
<div class="dots"><i class="on"></i><i></i><i></i></div>

<h2 class="section-title" style="left:196px;top:1950px">Get in <strong>Touch</strong></h2>
<p class="contact-intro">Would you like one of the torvex media &nbsp;team to give you a call or visit you on site to discuss your specific requirements? Fill in the form and we'll be in touch soon</p>
<div class="field" style="top:2060px">First name:</div>
<div class="field" style="top:2094px">Email address:</div>
<div class="field" style="top:2129px">Contact phone:</div>
<div class="field message">Massage</div>
<div class="submit-btn">SUBMIT</div>

<footer class="site-footer">
  <nav class="footer-nav"><span class="current">HOME</span>/<span>ABOUT US</span>/<span>SERVICES</span>/<span>NEWS</span>/<span>CONTACT</span></nav>
  <div class="copyright">copyright © 2014. Torvex media. All rights Reseverd</div>
  <div class="social">
    <span role="img" aria-label="Social profile link"></span>
    <span role="img" aria-label="Social profile link"></span>
    <span role="img" aria-label="Social profile link"></span>
    <span role="img" aria-label="Social profile link"></span>
  </div>
  <div class="footer-brand">
    <div class="brand-name">TORVEX Media</div>
    <div class="brand-tagline">Amplify every message that matters</div>
  </div>
</footer>

</body>
</html>
```